Community Bank Web Design

Design a homepage and internal product page for a community bank. Needs to be mobile friendly, minimal scrolling on home. Create the homepage look & feel, then use the same aesthetic to create the product page for the personal checking account page.

Wireframes, logo variations, and color scheme attached.

New brand identity:
• Open, Fresh, Younger, Bright, Bold, New, Innovative.
• Inviting, approachable, friendly, trustworthy.
• Imagine a young family purchasing their first home as the target audience.
You do not have to stick to the exact layout of the wireframes, as long as all of the elements are present.

All navigation elements are specified in wireframes. There are three versions of the homepage – Personal Home, Business Home, Wealth Management Home – you may design whichever version you prefer.

For internal page – please design the Checking product page, included in wireframes.

NOTE: Submit your homepage design first. I will provide feedback on your design direction, then you can use that to move forward with the internal page design.

Design direction--
Some banking / financial sites we like for their fresh/bold/open look:
velmorant.com
quendo.ca
rwxfinancial.org
pvt.co.nz
hopvault.com
pellerbank.com
ulk.co.nz

Target Market(s)

The target market for the personal homepage varies. Adults in the midwest, 25 - 60, who are striving to build their savings and manage their money. Often buying homes or refinancing their homes to make renovations, or planning for retirement.

For the business homepage, the target market are small to mid-market business owners striving to grow their business and manage their company.

Industry/Entity Type

Financial

Requirements
Must have
• colors: CRIMSON #a20c33,
FOREST GREEN #004f38
GOLD #e6a513

File format for design submission must be layered PSD (Please organize layers into recognizable folders like "menu" and "footer")

To make the design "mobile friendly" please create a grid-based layout. http://www.trovask.com/patterns/showPattern.php?patternID=grid-based-layout
http://www.quillbrightjournal.com/2007/04/14/designing-with-grid-based-approach/

```html
<!DOCTYPE html>
<html lang="en">
<head>
<meta charset="utf-8">
<title>Linden Ridge Bank – Personal</title>
<link href="https://fonts.googleapis.com/css2?family=Open+Sans:wght@400;600&display=swap" rel="stylesheet">
<style>
  :root{
    --crimson:#a20c33;
    --crimson-bright:#c20e3a;
    --crimson-dark:#8c0a2b;
    --forest:#004f38;
    --forest-line:#0b6a4d;
    --gold:#e6a513;
    --ink:#3d3d3d;
    --muted:#a3a3a3;
    --white:#ffffff;
  }
  *{box-sizing:border-box;margin:0;padding:0}
  html,body{width:1200px;height:1200px;overflow:hidden;background:var(--white)}
  body{font-family:"Open Sans",Arial,sans-serif;color:var(--ink);position:relative}
  a{color:inherit;text-decoration:none}

  .utility-nav{position:absolute;top:10px;left:132px;right:132px;display:flex;justify-content:space-between;font-size:12px;color:#444}
  .utility-nav ul{list-style:none;display:flex;gap:23px}

  .brand{position:absolute;top:50px;left:132px;display:flex;align-items:center;gap:8px}
  .brand-mark{width:36px;height:36px;border-radius:50%;background:var(--crimson)}
  .brand-name{font-size:23px;color:var(--crimson);font-weight:400;letter-spacing:-.3px}

  .search{position:absolute;top:59px;left:932px;width:136px;height:24px;border:1px solid var(--crimson);display:flex;align-items:center;padding:0 8px;gap:8px;font-size:11px;color:var(--crimson)}
  .search .clear{margin-left:auto}

  .main-nav{position:absolute;top:118px;left:132px;width:936px;height:40px;background:var(--crimson);display:flex;align-items:center;padding:0 24px;font-size:12px;color:var(--gold)}
  .main-nav ul{list-style:none;display:flex;gap:39px}
  .main-nav .login{margin-left:auto;display:flex;align-items:center;gap:8px}

  .login-panel{position:absolute;top:190px;left:132px;width:216px;height:301px;background:var(--crimson);color:var(--white);font-size:11px}
  .login-panel .label{position:absolute;top:20px;left:24px;font-size:12px}
  .field{position:absolute;left:24px;width:168px;height:27px;background:var(--crimson-dark);color:var(--gold);font-size:11px;display:flex;align-items:center;padding-left:11px}
  .field.type{top:48px}
  .field.type .arrow{margin-left:auto;width:28px;height:100%;border-left:1px solid var(--crimson);display:flex;align-items:center;justify-content:center}
  .field.user{top:91px}
  .forgot{position:absolute;top:131px;width:100%;text-align:center;font-size:10px;color:#d21848}
  .btn-login{position:absolute;top:169px;left:56px;width:104px;height:28px;background:var(--gold);display:flex;align-items:center;justify-content:center;gap:10px;font-size:11px}
  .new{position:absolute;top:214px;width:100%;text-align:center;font-size:11px}
  .enroll{position:absolute;top:240px;left:0;width:100%;display:flex;font-size:10px;color:var(--gold)}
  .enroll span{flex:1;text-align:center}
  .enroll span+span{border-left:1px solid #c4224a}
  .apply{position:absolute;bottom:0;left:0;width:100%;height:32px;background:var(--forest);display:flex;align-items:center;justify-content:center;font-size:11px}

  .hero{position:absolute;top:190px;left:372px;width:696px;height:301px;overflow:hidden}
  .hero-photo{position:absolute;inset:0 0 32px 0;background:linear-gradient(160deg,#8e8172 0%,#c9b79c 40%,#a8957c 60%,#5e4a37 100%)}
  .hero h1{position:absolute;top:38px;left:58px;font-size:33px;font-weight:600;color:var(--white);letter-spacing:.2px}
  .hero .sub{position:absolute;top:82px;left:58px;font-size:19px;font-weight:600;color:var(--white)}
  .hero .arrow{position:absolute;top:124px}
  .hero-bar{position:absolute;bottom:0;left:0;width:100%;height:32px;background:var(--forest);color:var(--white);font-size:11.5px;display:flex;align-items:center}
  .hero-bar p{padding-left:24px;flex:1}
  .hero-bar .more{width:122px;height:100%;border-left:1px solid var(--forest-line);display:flex;align-items:center;gap:10px;padding-left:18px}

  .feature-photo{position:absolute;top:555px;left:132px;width:240px;height:200px;background:linear-gradient(180deg,#8fae7a 0%,#c9d8b6 35%,#6e9d3d 65%,#3f7a20 100%)}
  .heloc{position:absolute;top:549px;left:396px;width:352px}
  h2{font-size:19px;font-weight:400;color:#444}
  .body-copy{font-size:11.5px;line-height:19.2px;color:var(--muted)}
  .heloc .body-copy{margin-top:14px}
  .btn{display:inline-block;background:var(--gold);color:var(--white);font-size:11.5px;height:27px;line-height:27px;padding:0 11px}
  .heloc .btn{position:absolute;top:179px}

  .rates{position:absolute;top:549px;left:771px;width:297px}
  .rates table{margin-top:14px;width:100%;border-collapse:collapse;background:var(--forest);color:var(--white);font-size:11.5px}
  .rates th{font-weight:400;height:33px;border-right:1px solid var(--forest-line);border-bottom:1px solid var(--forest-line)}
  .rates td{height:40px;padding-left:24px;border-bottom:1px solid var(--forest-line)}
  .rates td.rate{width:80px;padding-left:0;text-align:center;border-left:1px solid var(--forest-line)}
  .rates .body-copy{margin-top:17px}

  .promo{position:absolute;top:813px;width:300px}
  .promo .body-copy{margin-top:18px;width:160px}
  .promo .icon{position:absolute;top:64px;left:201px}
  .promo .btn{position:absolute;top:174px;left:1px}
  .promo h2{margin-left:-1px}

  .footer{position:absolute;top:1078px;left:0;width:1200px;height:122px;background:var(--crimson-bright);color:var(--white)}
  .footer .brand{top:28px;left:132px}
  .footer .brand-mark{background:var(--white)}
  .footer .brand-name{color:var(--white);font-size:22px}
  .footer-nav{position:absolute;top:43px;right:132px;list-style:none;display:flex;gap:31px;font-size:14px}
  .copyright{position:absolute;top:98px;left:132px;font-size:10px}
  .social{position:absolute;top:89px;right:132px;display:flex;gap:14px}
  .social span{width:20px;height:20px;border:1px solid var(--white);border-radius:50%}
</style>
</head>
<body>

<nav class="utility-nav">
  <ul><li>Personal</li><li>Business</li><li>Wealth Management</li></ul>
  <ul><li>Find a Branch or ATM</li><li>Contact Us</li></ul>
</nav>

<div class="brand"><span class="brand-mark"></span><span class="brand-name">Linden Ridge Bank</span></div>

<div class="search">
  <svg width="11" height="11" viewBox="0 0 12 12"><circle cx="7" cy="5" r="3.6" fill="none" stroke="#a20c33" stroke-width="1.6"/><line x1="4.4" y1="7.6" x2="1" y2="11" stroke="#a20c33" stroke-width="1.8"/></svg>
  <span>Search...</span>
  <svg class="clear" width="10" height="10" viewBox="0 0 10 10"><circle cx="5" cy="5" r="4.2" fill="none" stroke="#a20c33" stroke-width="1.3"/><circle cx="5" cy="5" r="2" fill="#a20c33"/></svg>
</div>

<nav class="main-nav">
  <ul><li>Products &amp; Services</li><li>Why LRB?</li><li>Customer Center</li></ul>
  <div class="login">
    <svg width="10" height="12" viewBox="0 0 10 12"><path d="M2.5 5V3.5a2.5 2.5 0 0 1 5 0V5" fill="none" stroke="#e6a513" stroke-width="1.5"/><rect x="0.5" y="5" width="9" height="7" fill="#e6a513"/></svg>
    <span>LOG IN</span>
  </div>
</nav>

<aside class="login-panel">
  <div class="label">Account type</div>
  <div class="field type">Banking
    <span class="arrow"><svg width="8" height="5" viewBox="0 0 8 5"><path d="M1 1l3 3 3-3" fill="none" stroke="#c4224a" stroke-width="1.3"/></svg></span>
  </div>
  <div class="field user">User ID</div>
  <div class="forgot">Forgot your User ID?</div>
  <div class="btn-login">
    <svg width="10" height="12" viewBox="0 0 10 12"><path d="M2.5 5V3.5a2.5 2.5 0 0 1 5 0V5" fill="none" stroke="#fff" stroke-width="1.5"/><rect x="0.5" y="5" width="9" height="7" fill="#fff"/></svg>
    <span>LOG IN</span>
  </div>
  <div class="new">New to LRB Online?</div>
  <div class="enroll"><span>ENROLL</span><span>LEARN MORE</span></div>
  <div class="apply">APPLY FOR A LOAN</div>
</aside>

<section class="hero">
  <div class="hero-photo" role="img" aria-label="A young couple seen from behind, looking at the front of a new brick and stucco house"></div>
  <h1>Dreaming of your first home?</h1>
  <p class="sub">Let's make it possible. Talk to a mortgage banker today.</p>
  <svg class="arrow" style="left:26px" width="20" height="30" viewBox="0 0 20 30"><path d="M16 3L4 15l12 12" fill="none" stroke="rgba(255,255,255,.7)" stroke-width="3"/></svg>
  <svg class="arrow" style="right:26px" width="20" height="30" viewBox="0 0 20 30"><path d="M4 3l12 12L4 27" fill="none" stroke="rgba(255,255,255,.7)" stroke-width="3"/></svg>
  <div class="hero-bar">
    <p>Sed ac purus et lectus aliquet tincidunt a eget mauris praesent dolor nunc.</p>
    <div class="more">
      <svg width="16" height="16" viewBox="0 0 16 16"><circle cx="8" cy="8" r="7" fill="none" stroke="#1f9a6e" stroke-width="1.2"/><path d="M7 5l3 3-3 3" fill="none" stroke="#1f9a6e" stroke-width="1.2"/></svg>
      <span>Learn More</span>
    </div>
  </div>
</section>

<div class="feature-photo" role="img" aria-label="A small house folded from banknotes standing on green grass"></div>

<article class="heloc">
  <h2>Home Equity Lines of Credit</h2>
  <p class="body-copy">Lorem ipsum dolor sit amet, consectetur adipiscing elit. Nulla quam velit, vulputate eu pharetra nec, mattis ac neque. Duis vulpu-tate commodo lectus, ac blandit elit tincidunt id. Sed rhoncus, tortor sed eleifend tristique, tortor mauris molestie elit, et lacinia ipsum quam nec dui. Quisque nec mauris sit amet elit iaculis pre-tium sit amet quis magna. Aenean velit odio, elementum in tempus ut, vehicula eu diam.</p>
  <a class="btn" href="#">Read More</a>
</article>

<section class="rates">
  <h2>Rates</h2>
  <table>
    <tr><th>Loans</th><th colspan="2" style="border-right:0">Deposits</th></tr>
    <tr><td>5 year fixed Mortgage</td><td class="rate">2.99%</td></tr>
    <tr><td style="border-bottom:0">Vantra Credit Card</td><td class="rate" style="border-bottom:0">8.24%</td></tr>
  </table>
  <p class="body-copy">Rates vary daily and depend on many factors. Call today to find your best options.</p>
</section>

<article class="promo" style="left:131px">
  <h2>Mobile Deposit. It's easy!</h2>
  <p class="body-copy">Lorem ipsum dolor sit amet, consectetur adipiscing elit. Nulla quam velit, vulputate eu pharetra nec, mattis ac neque. Duis vulputate commodo</p>
  <svg class="icon" width="56" height="54" viewBox="0 0 56 54" fill="none" stroke="#a20c33" stroke-width="2">
    <rect x="24" y="2" width="20" height="36" rx="3"/><line x1="30" y1="6" x2="38" y2="6"/>
    <path d="M24 22c-6 2-14 10-20 16l10 12c4-6 10-8 14-10"/><path d="M44 12h4M44 18h4M44 24h4"/>
  </svg>
  <a class="btn" href="#">Learn More</a>
</article>

<article class="promo" style="left:451px">
  <h2>Looking for a New Home?</h2>
  <p class="body-copy">Lorem ipsum dolor sit amet, consectetur adipiscing elit. Nulla quam velit, vulputate eu pharetra nec, mattis ac neque. Duis vulputate commodo</p>
  <svg class="icon" width="56" height="54" viewBox="0 0 56 54">
    <circle cx="32" cy="12" r="9" fill="#a20c33"/><circle cx="34" cy="10" r="2.5" fill="#fff"/>
    <path d="M26 18L4 40l4 4 3-3 3 3 3-3-3-3 15-15z" fill="#a20c33"/>
    <path d="M38 20l4 10-6 6 4 10h10l-2-10-6-6" fill="none" stroke="#a20c33" stroke-width="2"/>
  </svg>
  <a class="btn" href="#">Find your Mortgage Banker</a>
</article>

<article class="promo" style="left:771px">
  <h2>Vantra Debit Cards</h2>
  <p class="body-copy">Lorem ipsum dolor sit amet, consectetur adipiscing elit. Nulla quam velit, vulputate eu pharetra nec, mattis ac neque. Duis vulputate commodo</p>
  <svg class="icon" width="60" height="54" viewBox="0 0 60 54">
    <path d="M8 34l4 18 46-12-3-8" fill="none" stroke="#a20c33" stroke-width="2"/>
    <rect x="2" y="2" width="48" height="34" rx="3" fill="#a20c33"/>
    <rect x="8" y="9" width="7" height="6" fill="#fff"/><line x1="8" y1="24" x2="42" y2="24" stroke="#fff" stroke-width="1.5" stroke-dasharray="5 3"/>
    <circle cx="38" cy="10" r="4" fill="none" stroke="#fff" stroke-width="1.3"/><circle cx="43" cy="10" r="4" fill="none" stroke="#fff" stroke-width="1.3"/>
  </svg>
  <a class="btn" href="#">Learn More</a>
</article>

<footer class="footer">
  <div class="brand"><span class="brand-mark"></span><span class="brand-name">Linden Ridge Bank</span></div>
  <ul class="footer-nav">
    <li>About</li><li>Careers</li><li>Privacy Policy</li><li>Member FDIC</li><li>Investor Relations Link</li><li>Security</li><li>CRA</li>
  </ul>
  <p class="copyright">Copyright © 2014 Linden Ridge Bank. All Rights Reserved.</p>
  <div class="social" aria-label="Social links"><span></span><span></span><span></span></div>
</footer>

</body>
</html>
```